New Digital Marketing Company Needs Web Design

Introduction

Brightcrest gives advice to small businesses about their websites and digital marketing strategies and builds working relationships with clients to understand their business and maximise its online presence.

Brightcrest offers services to support its clients needs such as: website auditing & search engine optimisation (SEO), Quorvo Promoline, Chatterlane advertising, newsletter development & management, online performance reporting, email setup & management, website hosting, maintenance & backup, web development, web updates & web design.

Design Specification

The site should have a clean & professional look and use the colour scheme from the logo (attached below).

The design should consist of 2 templates; The homepage & content page.

Homepage Design

The homepage should have a header with logo, contact number and email and menu. Followed underneath by a slider and then individual blocks for key services. Under the key services should be a testimonial block with 3 testimonials. Finally the footer with company details, menu links and location map.

Header Info:

Contact number: 01632 960481
Email: info@brightcrest-demo.co.uk

Menu: Home Services About Contact

Slider Design:

The slider should be full page and show an image with text.

Key Services:

The key services should have a relevant icon and brief description.

The key services are:

Digital Marketing

Website Hosting & Management

Website Health Check (SEO)

Website Updating & Development

Newsletter Management

Email Management

Note: Lorem Ipsum can be used for brief description...

Testimonials:

There should be 3 testimonials side by side and they should include a headshot image of the person giving the testimonial.

Note: Lorem Ipsum and sample images can be used for testimonials...

Footer:

The footer should have 3 sections:

Menu links:

Digital Marketing About
Quorvo Promoline Contact
Chatterlane Advertising Privacy Policy
Search Engine Optimisation (SEO) Terms & Conditions
Website Hosting FAQ
Newsletter Management

Company Information:

BrightCrest
14 Marlow Close
Bracknell
Berskhire
ZZ9 4QT
Tel: 01632 960481

Chatterlane icon - Pipwave icon - Careernest icon

Location

Quorvo map

Footer Bottom:

Copyright message.

Content Design

The content design should have the common header and footer.

Each content page should have a banner for image with text description (page title).

The content page should have area for text description and area for a video display if available.

There should be a right column (possibly) for modules (latest blog, latest Chatterlane feeds, testimonial)

Project Deadline Extended
Reason: I have had to extend the deadline as could not review while on vacation and need to feedback to some designers for content page design. Many thanks for your understanding.

Target Market(s)

Industry/Entity Type

Digital

Number of Pages Required

2 page

Requirements
Must have
• The site should have a clean & professional look and use the colour scheme from the logo (attached below).
• The design should consist of 2 templates; The homepage & content page.

```html
<!DOCTYPE html>
<html lang="en">
<head>
<meta charset="utf-8">
<title>BrightCrest – Workshops, Services &amp; Support</title>
<link rel="stylesheet" href="https://fonts.googleapis.com/css2?family=Lato:ital,wght@0,400;0,700;0,900;1,400&family=Roboto+Slab:wght@400&display=swap">
<style>
:root{
  --plum:#6b1f52;
  --plum-dark:#5a1845;
  --indigo:#3f3566;
  --indigo-soft:#4b4170;
  --ink:#333;
  --muted:#555;
  --mist:#ececec;
  --pale:#f3f3f3;
  --night:#0c0c0c;
  --white:#fff;
  --disk:#dde3e8;
}
*{box-sizing:border-box;margin:0;padding:0}
html,body{width:1200px;height:2332px;overflow:hidden}
body{position:relative;font-family:'Lato',sans-serif;color:var(--ink);background:var(--white)}
.abs{position:absolute}

/* header */
.topbar{left:466px;top:0;width:734px;height:31px;background:var(--plum);clip-path:polygon(0 0,100% 0,100% 100%,30px 100%)}
.topbar-item{top:6px;color:var(--white);font-size:13px;display:flex;align-items:center;gap:8px}
.topbar-item.phone{font-size:17px;font-weight:700}
.brand{left:127px;top:24px;display:flex;align-items:center;gap:10px}
.brand-dot{width:36px;height:36px;border-radius:50%;background:var(--plum)}
.brand-name{font-size:38px;font-weight:900;color:var(--plum);letter-spacing:-.5px}
.nav{top:54px;left:0;width:1200px;height:20px;font-size:14px;color:var(--indigo)}
.nav a{position:absolute;color:inherit;text-decoration:none;text-transform:uppercase}
.nav a.active{border-bottom:2px solid var(--plum);padding-bottom:4px}

/* hero */
.hero{left:0;top:95px;width:1200px;height:440px;background:linear-gradient(110deg,#3d4043 0%,#55585b 45%,#3a3c3f 100%)}
.hero-arrow{top:285px;width:34px;height:30px;background:#2a2a2a;display:flex;align-items:center;justify-content:center}
.hero-caption{left:0;top:482px;width:1200px;height:53px;background:rgba(20,20,20,.72)}
.hero-text{left:219px;top:494px;font-family:'Roboto Slab',serif;font-size:23px;color:var(--white)}
.hero-btn{left:851px;top:492px;width:150px;height:37px;background:var(--indigo-soft);color:var(--white);font-size:21px;font-weight:700;display:flex;align-items:center;justify-content:center}

/* section headings */
.section-title{left:0;width:1200px;text-align:center;font-size:32px;font-weight:700;color:var(--plum)}
.section-title.light{font-weight:400}
.divider{left:393px;width:414px;height:14px}
.divider::before,.divider::after{content:"";position:absolute;top:7px;width:190px;height:1px;background:#aaa}
.divider::before{left:0}.divider::after{right:0}
.divider span{position:absolute;left:200px;top:0;width:14px;height:14px;border-radius:50%;border:2px solid var(--plum)}

/* welcome */
.welcome{left:0;top:535px;width:1200px;height:281px;background:var(--mist)}
.welcome-text{left:137px;top:662px;width:926px;text-align:center;font-size:11.5px;line-height:18px;color:var(--muted)}
.read-more{left:544px;top:744px;width:112px;height:31px;border-radius:16px;background:var(--plum);color:var(--white);font-size:12px;font-weight:700;display:flex;align-items:center;justify-content:center}

/* services */
.service-label{font-size:11.5px;line-height:15px;color:var(--muted)}
.service-label h3{font-size:15.5px;font-weight:700;color:var(--indigo);margin-bottom:4px}
.service-label.right{text-align:right}
.service-label.right h3{color:var(--plum)}
.service-label.right.indigo h3{color:var(--indigo)}

/* testimonials */
.testimonials{left:0;top:1596px;width:1200px;height:430px;background:var(--pale)}
.t-card{top:1750px;width:300px;text-align:center}
.t-photo{margin:0 auto;width:110px;height:104px;border:3px solid var(--plum);border-radius:4px;background:linear-gradient(160deg,#c9d6e2,#8aa0b4)}
.t-quote{margin-top:30px;font-style:italic;font-size:12.5px;line-height:15.5px;color:var(--ink);padding:0 32px}
.t-name{margin-top:10px;font-size:14px;font-weight:700;color:var(--plum)}
.t-mark{font-family:Georgia,serif;font-size:110px;line-height:1;color:#d9d9d9}
.t-arrow{top:1808px}

/* footer */
.footer{left:0;top:2026px;width:1200px;height:264px;background:var(--night)}
.f-head{top:2060px;font-size:16px;color:var(--white);padding-bottom:8px;border-bottom:1px solid #333;width:185px;font-weight:400}
.f-head span{color:var(--plum)}
.f-list{top:2096px;list-style:none;font-size:11.5px;line-height:15px;color:#ddd}
.f-list li{margin-bottom:9px;padding-left:9px;position:relative}
.f-list li::before{content:"";position:absolute;left:0;top:6px;width:3px;height:3px;background:#888}
.f-contact{font-size:11.5px;line-height:16px;color:#ddd}
.f-map{left:634px;top:2099px;width:237px;height:154px;background:linear-gradient(135deg,#e9e6df,#d6d3cb)}
.f-social{left:929px;display:flex;align-items:flex-start;gap:14px}
.f-social i{display:block;width:31px;height:31px;border-radius:50%;background:var(--plum)}
.f-social b{display:block;font-size:12.5px;font-weight:400;color:var(--white);margin-top:4px}
.f-social small{display:block;font-size:8.5px;color:#777;letter-spacing:.5px;margin-top:6px}
.copyright{left:0;top:2290px;width:1200px;height:42px;background:var(--plum);color:var(--white);font-size:12px;display:flex;align-items:center;justify-content:center}
</style>
</head>
<body>

<header>
  <div class="abs topbar"></div>
  <div class="abs topbar-item" style="left:713px">
    <svg width="15" height="11" viewBox="0 0 15 11"><rect x="0" y="0" width="15" height="11" fill="#fff"/><path d="M0 0L7.5 6 15 0" fill="none" stroke="#6b1f52" stroke-width="1.4"/></svg>
    info@brightcrest-demo.co.uk
  </div>
  <div class="abs topbar-item phone" style="left:930px;top:4px">
    <svg width="22" height="22" viewBox="0 0 22 22"><circle cx="11" cy="11" r="10" fill="none" stroke="#fff" stroke-width="1.5"/><path d="M8 6c-1 1-1 3 1 6s4 4 5 3l1-1-2-2-1 1c-1 0-3-2-3-3l1-1-2-2z" fill="#fff"/></svg>
    01632 960481
  </div>
  <div class="abs brand"><span class="brand-dot"></span><span class="brand-name">BrightCrest</span></div>
  <nav class="abs nav">
    <a class="active" href="#" style="left:554px">Home</a>
    <a href="#" style="left:660px">About Us</a>
    <a href="#" style="left:797px">Our Services</a>
    <a href="#" style="left:973px">Contact Us</a>
  </nav>
</header>

<section>
  <div class="abs hero" role="img" aria-label="Businessman in a suit facing a chalkboard covered with marketing sketches"></div>
  <div class="abs hero-arrow" style="left:0"><svg width="10" height="12"><path d="M8 1L2 6l6 5" fill="none" stroke="#fff" stroke-width="2"/></svg></div>
  <div class="abs hero-arrow" style="left:1166px"><svg width="10" height="12"><path d="M2 1l6 5-6 5" fill="none" stroke="#fff" stroke-width="2"/></svg></div>
  <div class="abs hero-caption"></div>
  <div class="abs hero-text">Workshops, Services &amp; Support For The Small Business</div>
  <div class="abs hero-btn">Get Started</div>
</section>

<section>
  <div class="abs welcome"></div>
  <h1 class="abs section-title" style="top:577px">Welcome to <span style="color:var(--indigo)">BrightCrest</span></h1>
  <div class="abs divider" style="top:627px"><span></span></div>
  <p class="abs welcome-text">Lorem ipsum dolor sit amet, consectetuer adipiscing elit, sed diam nonummy nibh euismod tincidunt ut laoreet dolore magna aliquam erat volutpat. Ut wisi enim ad minim veniam, lobortis nisl ut aliquip ex ea commodo consequat. Duis autem vel eum iriure dolor in hendrerit in vulputate velit esse molestie eros et dignissim qui blandit praesent luptatum zzril delenit augue duis dolore te feugait nulla facilisi.</p>
  <div class="abs read-more">READ MORE</div>
</section>

<section>
  <h2 class="abs section-title" style="top:863px;color:var(--indigo);font-weight:400">Our Services</h2>
  <div class="abs divider" style="top:913px"><span></span></div>

  <svg class="abs" style="left:0;top:0" width="1200" height="1596" viewBox="0 0 1200 1596">
    <defs>
      <filter id="lift" x="-30%" y="-30%" width="160%" height="160%"><feDropShadow dx="0" dy="3" stdDeviation="4" flood-opacity=".3"/></filter>
    </defs>
    <circle cx="600" cy="1228" r="163" fill="var(--disk)"/>
    <circle cx="600" cy="1228" r="40" fill="none" stroke="#b9b4c6" stroke-width="8"/>
    <g stroke="#999" stroke-width="1" fill="#666">
      <line x1="416" y1="1113" x2="395" y2="1068"/><circle cx="416" cy="1113" r="2.5"/>
      <line x1="659" y1="1023" x2="676" y2="998"/><circle cx="659" cy="1023" r="2.5"/>
      <line x1="818" y1="1189" x2="860" y2="1210"/><circle cx="818" cy="1189" r="2.5"/>
      <line x1="818" y1="1369" x2="855" y2="1392"/><circle cx="818" cy="1369" r="2.5"/>
      <line x1="549" y1="1474" x2="526" y2="1518"/><circle cx="549" cy="1474" r="2.5"/>
      <line x1="385" y1="1295" x2="368" y2="1258"/><circle cx="385" cy="1295" r="2.5"/>
    </g>
    <g filter="url(#lift)">
      <circle cx="600" cy="1080" r="56" fill="#fff"/><circle cx="600" cy="1080" r="49" fill="var(--indigo-soft)"/>
      <circle cx="737" cy="1169" r="56" fill="#fff"/><circle cx="737" cy="1169" r="49" fill="var(--indigo-soft)"/>
      <circle cx="737" cy="1329" r="56" fill="#fff"/><circle cx="737" cy="1329" r="49" fill="var(--indigo-soft)"/>
      <circle cx="600" cy="1410" r="56" fill="#fff"/><circle cx="600" cy="1410" r="49" fill="var(--indigo-soft)"/>
      <circle cx="448" cy="1329" r="56" fill="#fff"/><circle cx="448" cy="1329" r="49" fill="var(--indigo-soft)"/>
      <circle cx="448" cy="1169" r="56" fill="#fff"/><circle cx="448" cy="1169" r="49" fill="var(--plum)"/>
    </g>
    <g fill="none" stroke="#fff" stroke-width="3" stroke-linecap="round">
      <circle cx="600" cy="1080" r="16"/><circle cx="600" cy="1080" r="6"/>
      <path d="M600 1058v6M600 1096v6M578 1080h6M616 1080h6M584 1064l4 4M612 1092l4 4M584 1096l4-4M612 1068l4-4"/>
      <rect x="715" y="1156" width="44" height="30"/><path d="M715 1156l22 17 22-17M715 1186l16-14M759 1186l-16-14"/>
      <circle cx="728" cy="1314" r="9" fill="#fff"/><path d="M712 1348c0-14 8-20 16-20s16 6 16 20z" fill="#fff"/>
      <rect x="738" y="1330" width="22" height="15" fill="var(--indigo-soft)"/><path d="M738 1330l11 8 11-8"/>
      <rect x="587" y="1390" width="20" height="38" rx="3"/><path d="M614 1402q6 8 0 16M620 1397q10 13 0 26"/>
      <path d="M428 1330a10 10 0 0 1 6-18a14 14 0 0 1 27 2a9 9 0 0 1 2 17z"/><rect x="437" y="1336" width="22" height="7"/><rect x="437" y="1345" width="22" height="7"/>
      <circle cx="452" cy="1163" r="13"/><path d="M461 1172l12 12" stroke-width="5"/>
    </g>
    <text x="418" y="1169" font-family="Lato,sans-serif" font-weight="900" font-size="16" fill="#fff">SEO</text>
  </svg>

  <div class="abs service-label right" style="left:150px;top:994px;width:246px"><h3>Website Health Check (SEO)</h3>Sed ut perspiciatis unde omnis<br>sit voluptatem accusantium</div>
  <div class="abs service-label" style="left:688px;top:971px"><h3>Website Updating &amp; Development</h3>Sed ut perspiciatis unde omnis<br>sit voluptatem accusantium</div>
  <div class="abs service-label right indigo" style="left:100px;top:1182px;width:273px"><h3>Website Hosting &amp; Management</h3>Sed ut perspiciatis unde omnis<br>sit voluptatem accusantium</div>
  <div class="abs service-label" style="left:875px;top:1205px"><h3>Newsletter Management</h3>Sed ut perspiciatis unde omnis<br>sit voluptatem accusantium</div>
  <div class="abs service-label" style="left:867px;top:1393px"><h3>Email Management</h3>Sed ut perspiciatis unde omnis<br>sit voluptatem accusantium</div>
  <div class="abs service-label right indigo" style="left:257px;top:1497px;width:250px"><h3>Digital Marketing</h3>Sed ut perspiciatis unde omnis<br>sit voluptatem accusantium</div>
</section>

<section>
  <div class="abs testimonials"></div>
  <h2 class="abs section-title light" style="top:1634px">Client Testimonials</h2>
  <div class="abs divider" style="top:1680px"><span></span></div>
  <svg class="abs t-arrow" style="left:101px" width="16" height="28"><path d="M14 2L3 14l11 12" fill="none" stroke="#6b1f52" stroke-width="3"/></svg>
  <svg class="abs t-arrow" style="left:1077px" width="16" height="28"><path d="M2 2l11 12L2 26" fill="none" stroke="#6b1f52" stroke-width="3"/></svg>

  <div class="abs t-mark" style="left:140px;top:1830px">“</div>
  <div class="abs t-mark" style="left:452px;top:1830px">“</div>
  <div class="abs t-mark" style="left:768px;top:1830px">“</div>

  <div class="abs t-card" style="left:122px">
    <div class="t-photo" role="img" aria-label="Headshot of a smiling client"></div>
    <p class="t-quote">Lorem ipsum dolor sit amet, consecer adscing elit, sed diam nonummy Lorem ipsum dolor sit amet, consectetuer adipiscing elit,</p>
    <p class="t-name">- Consectetue Radipiscing</p>
  </div>
  <div class="abs t-card" style="left:456px">
    <div class="t-photo" role="img" aria-label="Headshot of a client in a shirt and tie"></div>
    <p class="t-quote">Lorem ipsum dolor sit amet, consectetuer adipiscing elit, sed diam nonummy Lorem ipsum dolor sit amet, consectetuer adipiscing elit,</p>
    <p class="t-name">- Diam Nonummy</p>
  </div>
  <div class="abs t-card" style="left:772px">
    <div class="t-photo" role="img" aria-label="Headshot of a senior client in a suit"></div>
    <p class="t-quote">Lorem ipsum dolor sit amet, consectetuer adipiscing elit, sed diam nonummy Lorem ipsum dolor sit amet, consectetuer adipiscing elit,</p>
    <p class="t-name">- Dolor Sitamet</p>
  </div>
</section>

<footer>
  <div class="abs footer"></div>

  <h4 class="abs f-head" style="left:130px">Quick <span>Links</span></h4>
  <ul class="abs f-list" style="left:130px">
    <li>Digital Marketing About</li>
    <li>Quorvo Promoline Contact</li>
    <li>Chatterlane Advertising<br>Privacy Policy</li>
    <li>Search Engine Optimisation (SEO)<br>Terms &amp; Conditions</li>
    <li>Website Hosting FAQ</li>
    <li>Newsletter Management</li>
  </ul>

  <h4 class="abs f-head" style="left:385px">Contact <span>Details</span></h4>
  <svg class="abs" style="left:393px;top:2098px" width="12" height="16"><path d="M6 15C2 9 1 7 1 5a5 5 0 0 1 10 0c0 2-1 4-5 10z" fill="#6b1f52"/><circle cx="6" cy="5" r="2" fill="#0c0c0c"/></svg>
  <p class="abs f-contact" style="left:418px;top:2096px">BrightCrest<br>14 Marlow Close<br>Hollowmere Daleshire<br>ZZ9 4QT</p>
  <svg class="abs" style="left:393px;top:2194px" width="12" height="12"><path d="M2 1c-2 2 0 6 3 8s6 4 7 1l-3-2-1 1C6 8 4 6 4 5l1-1-2-3z" fill="#6b1f52"/></svg>
  <p class="abs f-contact" style="left:418px;top:2192px">01632 960481</p>
  <svg class="abs" style="left:393px;top:2245px" width="12" height="9"><rect width="12" height="9" fill="#6b1f52"/><path d="M0 0l6 5 6-5" fill="none" stroke="#0c0c0c"/></svg>
  <p class="abs f-contact" style="left:418px;top:2241px">info@brightcrest-demo.co.uk</p>

  <h4 class="abs f-head" style="left:631px;width:240px">Location <span>Map</span></h4>
  <div class="abs f-map" role="img" aria-label="Street map showing the office location"></div>

  <h4 class="abs f-head" style="left:929px;width:136px">Follow <span>Us</span></h4>
  <div class="abs f-social" style="top:2102px"><i></i><div><b>CHATTERLANE</b><small>BECOME A FAN</small></div></div>
  <div class="abs f-social" style="top:2163px"><i></i><div><b>CAREERNEST</b><small>FOLLOW US</small></div></div>
  <div class="abs f-social" style="top:2220px"><i></i><div><b>PIPWAVE</b><small>JOIN US ON</small></div></div>

  <div class="abs copyright">© 2016 Brightcrest.All Rights Reserved.</div>
</footer>

</body>
</html>
```